Swiss Consultant for Enterprises and SME's is in Need for PPT for Teaching/Presenting

I am looking for a powerpointpresentation template (must be with slidemaster) for presenting my company and also for teaching. Colors must be taken from Logo and content can be taken from website if needed.

It is either used to present anything regarding finances and ERP-Systemrelated topics (espeically VEX Trade Suite) and also teach anything regarding Finance and or ERP-Systems in an industrial or financial environment.
Updates

Low design quality

Font styles to use
Sans Serif

Requirements
Must have
• I need at least following slides (Title, Subtitle/Section, Index, Single content, Empty (just logo), two content, tree content -> each as column and at last 4 / 5 & 6 infographics (done with o365 "standard" Icons)
• Coloring white and same as logo provided no additional colors except for charts etc.(matching to logostyle)
• Also I need a Word template such as the one attached.
Nice to have
• any additional infographic
Should not have
• Presentation must be done in the slidemaster as a template anything else will not be accepted.
• Letterhead is not needed I only need a Document for Documentation.

```html
<!DOCTYPE html>
<html lang="en">
<head>
<meta charset="utf-8">
<title>Alpenrand Consulting – Slide Template Overview</title>
<link href="https://fonts.googleapis.com/css2?family=Roboto:wght@400;500;700;900&display=swap" rel="stylesheet">
<style>
  :root{
    --blue:#0a6ac2;
    --blue-dark:#0656a8;
    --blue-mid:#2a8fd4;
    --cyan:#2ae3d4;
    --lime:#b9dc55;
    --green:#8cc63f;
    --yellow:#ffe600;
    --amber:#ffc61a;
    --red:#e84a2e;
    --ink:#6b6b6b;
    --ink-dark:#333;
    --frame:#d4d4d4;
    --paper:#ffffff;
  }
  html,body{margin:0;padding:0;background:var(--paper);overflow:hidden;}
  .sheet{position:relative;width:1200px;height:1200px;overflow:hidden;background:var(--paper);font-family:'Roboto',sans-serif;}
  .slide{position:absolute;width:370px;height:278px;box-shadow:0 0 0 1px var(--frame),1px 2px 3px rgba(0,0,0,.15);background:var(--paper);}
  .slide svg{display:block;width:100%;height:100%;}
  .c1{left:24px}.c2{left:415px}.c3{left:806px}
  .r1{top:16px}.r2{top:311px}.r3{top:608px}.r4{top:905px}
  svg text{font-family:'Roboto',sans-serif;}
  .logo{fill:var(--blue);font-size:17px;font-weight:500;}
  .logo-mark{fill:var(--blue);}
  .title{fill:var(--blue);font-size:12px;font-weight:500;}
  .body{fill:var(--ink);font-size:4.6px;}
  .label{fill:var(--ink-dark);font-size:4.8px;font-weight:700;}
  .on-color{fill:#fff;font-size:6px;font-weight:700;}
  .num{fill:#fff;font-size:8px;font-weight:700;}
  .hero{font-size:46px;font-weight:900;fill:#fff;}
  .hero-accent{fill:var(--yellow);}
  .url{fill:var(--blue);font-size:6px;letter-spacing:1.2px;}
  .line{stroke:var(--blue);fill:none;}
  .icon{stroke:var(--blue);fill:none;stroke-width:1.6;stroke-linecap:round;stroke-linejoin:round;}
  .icon-w{stroke:#fff;fill:none;stroke-width:2.2;stroke-linecap:round;stroke-linejoin:round;}
</style>
</head>
<body>
<div class="sheet">

  <!-- Title slide -->
  <div class="slide c1 r1">
    <svg viewBox="0 0 462 348">
      <polygon points="0,0 60,0 0,150" fill="var(--blue)"/>
      <polygon points="270,0 462,0 462,150 215,150" fill="#4b6d8c" role="img" aria-label="Photo of alpine peaks above clouds at sunset"/>
      <polygon points="270,0 462,0 462,70 240,70" fill="#c77a6a" opacity=".55"/>
      <rect x="0" y="150" width="462" height="103" fill="var(--blue)"/>
      <polygon points="385,348 462,348 462,253 440,253" fill="var(--blue)"/>
      <rect x="78" y="62" width="7" height="7" class="logo-mark"/>
      <text x="90" y="76" class="logo" style="font-size:30px">Alpenrand</text>
      <text x="34" y="220" class="hero"><tspan class="hero-accent">PRE</tspan>SENTATION</text>
      <text x="180" y="325" class="url">www.alpenrand-consult.ch</text>
    </svg>
  </div>

  <!-- Image and text slide -->
  <div class="slide c2 r1">
    <svg viewBox="0 0 462 348">
      <defs><linearGradient id="snow" x1="0" y1="0" x2="0" y2="1"><stop offset="0" stop-color="#1a4fd8"/><stop offset=".45" stop-color="#9aa6e8"/><stop offset="1" stop-color="#1c5ce0"/></linearGradient></defs>
      <rect x="0" y="0" width="260" height="348" fill="url(#snow)" role="img" aria-label="Photo of snowy mountain landscape in blue light"/>
      <rect x="192" y="40" width="108" height="36" fill="#fff"/>
      <text x="205" y="64" class="title">Lorem Ipsum is</text>
      <rect x="353" y="40" width="5" height="5" class="logo-mark"/>
      <text x="358" y="50" class="logo">Alpenrand</text>
      <g class="body">
        <text x="282" y="98">Short note on the topic for the team.</text>
        <text x="282" y="110">Key points shown in a simple layout.</text>
        <text x="282" y="122">Each item kept brief and to the point.</text>
        <text x="282" y="134">Content taken from the firm website.</text>
        <text x="282" y="146">Used for finance and system topics.</text>
        <text x="282" y="158">Also used when teaching in class.</text>
        <text x="282" y="170">Short note on the topic for the team.</text>
        <text x="282" y="182">Key points shown in a simple layout.</text>
        <text x="282" y="194">Each item kept brief and to the point.</text>
        <text x="282" y="206">Content taken from the firm website.</text>
        <text x="282" y="218">Used for finance and system topics.</text>
        <text x="282" y="230">Also used when teaching in class.</text>
        <text x="282" y="242">Short note on the topic for the team.</text>
        <text x="282" y="254">Key points shown in a simple layout.</text>
        <text x="282" y="266">Each item kept brief and to the point.</text>
      </g>
    </svg>
  </div>

  <!-- Single content with photo -->
  <div class="slide c3 r1">
    <svg viewBox="0 0 462 348">
      <polygon points="0,0 60,0 0,140" fill="var(--blue)"/>
      <polygon points="42,80 295,80 235,312 0,312 0,190" fill="#b9b4ae" role="img" aria-label="Photo of an office worker at a laptop"/>
      <polygon points="400,348 462,348 462,250" fill="var(--blue)"/>
      <text x="75" y="62" class="title">Lorem Ipsum is simply</text>
      <rect x="352" y="40" width="5" height="5" class="logo-mark"/>
      <text x="357" y="50" class="logo">Alpenrand</text>
      <g class="body">
        <text x="280" y="154">Short note on the topic for the team.</text>
        <text x="280" y="167">Key points shown in a simple layout.</text>
        <text x="280" y="180">Each item kept brief and clear.</text>
        <text x="280" y="193">Content taken from the firm website.</text>
        <text x="280" y="206">Used for finance and system topics.</text>
        <text x="280" y="219">Also used when teaching in class.</text>
        <text x="280" y="232">Short note on the topic for the team.</text>
        <text x="280" y="245">Key points shown in a simple layout.</text>
        <text x="280" y="258">Each item kept brief and clear.</text>
      </g>
    </svg>
  </div>

  <!-- Two content with banner -->
  <div class="slide c1 r2">
    <svg viewBox="0 0 462 348">
      <rect x="0" y="0" width="462" height="8" fill="var(--blue)"/>
      <text x="168" y="50" class="title">Lorem Ipsum is simply</text>
      <rect x="352" y="36" width="5" height="5" class="logo-mark"/>
      <text x="357" y="46" class="logo">Alpenrand</text>
      <rect x="0" y="67" width="462" height="124" fill="#6f92b4" role="img" aria-label="Photo of snow-capped Alps above green forest"/>
      <rect x="0" y="150" width="462" height="41" fill="#4f6b3a"/>
      <g class="body">
        <text x="30" y="212"><tspan class="label">Lorem Ipsum</tspan> is a short note on the topic here.</text>
        <text x="30" y="220">Key points are shown in a simple layout for all.</text>
        <text x="30" y="228">Each item is kept brief and to the point here.</text>
        <text x="30" y="236">Content is taken from the firm website pages.</text>
        <text x="30" y="244">It is used for finance and system topics too.</text>
        <text x="30" y="252">It is also used when teaching in the class.</text>
        <text x="30" y="260">Key points are shown in a simple layout for all.</text>
        <text x="30" y="268">Each item is kept brief and to the point here.</text>
        <text x="235" y="212">Key points are shown in a simple layout for all.</text>
        <text x="235" y="220">Each item is kept brief and to the point here.</text>
        <text x="235" y="228">Content is taken from the firm website pages.</text>
        <text x="235" y="236">It is used for finance and system topics too.</text>
        <text x="235" y="244">It is also used when teaching in the class.</text>
        <text x="235" y="252">Key points are shown in a simple layout for all.</text>
        <text x="235" y="260">Each item is kept brief and to the point here.</text>
      </g>
      <rect x="0" y="336" width="462" height="8" fill="var(--yellow)"/>
    </svg>
  </div>

  <!-- Four icon points -->
  <div class="slide c2 r2">
    <svg viewBox="0 0 462 348">
      <text x="166" y="50" class="title">Lorem Ipsum is simply</text>
      <rect x="353" y="36" width="5" height="5" class="logo-mark"/>
      <text x="358" y="46" class="logo">Alpenrand</text>
      <g class="body">
        <text x="68" y="99" class="label">Lorem Ipsum</text>
        <text x="68" y="110">is a short note on the topic and</text>
        <text x="68" y="118">the key points shown in a simple</text>
        <text x="68" y="126">layout for the team to read.</text>
        <text x="68" y="134">Kept brief since 2016.</text>
        <text x="273" y="99" class="label">Lorem Ipsum</text>
        <text x="273" y="110">is a short note on the topic and</text>
        <text x="273" y="118">the key points shown in a simple</text>
        <text x="273" y="126">layout for the team to read.</text>
        <text x="273" y="134">Kept brief since 2016.</text>
        <text x="169" y="194" class="label">Lorem Ipsum</text>
        <text x="169" y="205">is a short note on the topic and</text>
        <text x="169" y="213">the key points shown in a simple</text>
        <text x="169" y="221">layout for the team to read.</text>
        <text x="169" y="229">Kept brief since 2016.</text>
      </g>
      <g class="icon">
        <path d="M222,106 a11,11 0 1 1 16,0 c-3,3 -3,5 -3,8 h-10 c0,-3 0,-5 -3,-8z"/>
        <path d="M225,119 h10 M226,123 h8 M228,127 h4"/>
        <path d="M230,82 v-5 M214,89 l-4,-3 M246,89 l4,-3 M210,103 h-5 M250,103 h5"/>
      </g>
      <rect x="65" y="160" width="330" height="9" fill="var(--cyan)"/>
      <rect x="183" y="160" width="95" height="9" fill="var(--blue-mid)"/>
      <g class="icon">
        <rect x="82" y="193" width="28" height="28" rx="3"/>
        <path d="M92,214 l2,-7 15,-15 5,5 -15,15 -7,2z"/>
        <circle cx="350" cy="210" r="5"/>
        <path d="M350,196 v4 M350,220 v4 M336,210 h4 M360,210 h4 M340,200 l3,3 M357,217 l3,3 M360,200 l-3,3 M343,217 l-3,3"/>
        <circle cx="350" cy="210" r="10"/>
      </g>
    </svg>
  </div>

  <!-- Two column with building -->
  <div class="slide c3 r2">
    <svg viewBox="0 0 462 348">
      <polygon points="0,0 160,0 65,210 190,348 0,348" fill="#7da6c4" role="img" aria-label="Photo of glass office towers against blue sky"/>
      <text x="158" y="51" class="title">Lorem Ipsum is simply</text>
      <rect x="352" y="37" width="5" height="5" class="logo-mark"/>
      <text x="357" y="47" class="logo">Alpenrand</text>
      <line x1="150" y1="64" x2="462" y2="64" class="line" stroke-width="1.5"/>
      <g class="body">
        <text x="158" y="94"><tspan class="label">Lorem Ipsum</tspan> is a short note here.</text>
        <text x="158" y="102">Key points shown in a simple layout.</text>
        <text x="158" y="110">Each item kept brief and clear.</text>
        <text x="158" y="118">Content taken from the firm website.</text>
        <text x="158" y="126">Used for finance and system topics.</text>
        <text x="158" y="134">Also used when teaching in class.</text>
        <text x="158" y="142">Key points shown in a simple layout.</text>
        <text x="158" y="150">Each item kept brief and clear.</text>
        <text x="158" y="166">Content taken from the firm website.</text>
        <text x="158" y="174">Used for finance and system topics.</text>
        <text x="158" y="182">Also used when teaching in class.</text>
        <text x="158" y="190">Key points shown in a simple layout.</text>
        <text x="158" y="198">Each item kept brief and clear.</text>
        <text x="158" y="206">Content taken from the firm website.</text>
        <text x="158" y="214">Used for finance and system topics.</text>
        <text x="158" y="222">Also used when teaching in class.</text>
        <text x="158" y="230">Key points shown in a simple layout.</text>
        <text x="158" y="238">Each item kept brief and clear.</text>
        <text x="158" y="246">Content taken from the firm website.</text>
        <text x="158" y="254">Used for finance and system topics.</text>
        <text x="158" y="262">Also used when teaching in class.</text>
        <text x="300" y="94">Short intro line for this column.</text>
        <text x="300" y="102">Kept brief.</text>
        <text x="300" y="118">Key points shown in a simple layout.</text>
        <text x="300" y="126">Each item kept brief and clear.</text>
        <text x="300" y="134">Content taken from the firm website.</text>
        <text x="300" y="142">Used for finance and system topics.</text>
        <text x="300" y="150">Also used when teaching in class.</text>
        <text x="300" y="158">Key points shown in a simple layout.</text>
        <text x="300" y="166">Each item kept brief and clear.</text>
        <text x="300" y="174">Content taken from the firm website.</text>
        <text x="300" y="182">Used for finance and system topics.</text>
        <text x="300" y="190">Also used when teaching in class.</text>
        <text x="300" y="198">Key points shown in a simple layout.</text>
        <text x="300" y="206">Each item kept brief and clear.</text>
        <text x="300" y="214">Content taken from the firm website.</text>
        <text x="300" y="222">Used for finance and system topics.</text>
      </g>
    </svg>
  </div>

  <!-- Process arrows -->
  <div class="slide c1 r3">
    <svg viewBox="0 0 462 348">
      <text x="62" y="50" class="title">Lorem Ipsum is simply</text>
      <rect x="352" y="36" width="5" height="5" class="logo-mark"/>
      <text x="357" y="46" class="logo">Alpenrand</text>
      <polygon points="58,96 388,96 388,83 413,108 388,133 388,120 58,120" fill="var(--blue)"/>
      <polygon points="141,122 388,122 388,112 413,134 388,156 388,146 141,146" fill="var(--cyan)"/>
      <polygon points="225,148 388,148 388,138 413,160 388,182 388,172 225,172" fill="var(--amber)"/>
      <polygon points="307,174 388,174 388,160 413,187 388,214 388,200 307,200" fill="var(--red)"/>
      <text x="70" y="111" class="on-color">Main Idea</text>
      <text x="150" y="137" class="on-color">Research</text>
      <text x="233" y="163" fill="var(--ink-dark)" style="font-size:6px;font-weight:700">Set the Time</text>
      <text x="313" y="190" class="on-color">Delivery</text>
      <g class="body">
        <text x="62" y="130">Short note on</text><text x="62" y="138">the step and its</text><text x="62" y="146">key points kept</text><text x="62" y="154">brief for the team.</text><text x="62" y="162">Used since 2016.</text>
        <text x="146" y="156">Short note on</text><text x="146" y="164">the step and its</text><text x="146" y="172">key points kept</text><text x="146" y="180">brief for the team.</text><text x="146" y="188">Used since 2016.</text>
        <text x="229" y="182">Short note on</text><text x="229" y="190">the step and its</text><text x="229" y="198">key points kept</text><text x="229" y="206">brief for the team.</text><text x="229" y="214">Used since 2016.</text>
        <text x="311" y="208">Short note on</text><text x="311" y="216">the step and its</text><text x="311" y="224">key points kept</text><text x="311" y="232">brief for the team.</text><text x="311" y="240">Used since 2016.</text>
      </g>
    </svg>
  </div>

  <!-- Chevron list -->
  <div class="slide c2 r3">
    <svg viewBox="0 0 462 348">
      <text x="46" y="50" class="title">Lorem Ipsum is simply</text>
      <rect x="353" y="36" width="5" height="5" class="logo-mark"/>
      <text x="358" y="46" class="logo">Alpenrand</text>
      <rect x="130" y="82" width="285" height="58" fill="none" stroke="var(--blue)"/>
      <rect x="130" y="148" width="285" height="58" fill="none" stroke="var(--green)"/>
      <rect x="130" y="214" width="285" height="58" fill="none" stroke="var(--cyan)"/>
      <polygon points="42,82 72,102 130,82 130,148 72,168 42,148" fill="var(--blue)"/>
      <polygon points="42,148 72,168 130,148 130,214 72,234 42,214" fill="var(--green)"/>
      <polygon points="42,214 72,234 130,214 130,278 86,298 42,278" fill="var(--cyan)"/>
      <text x="56" y="130" class="on-color">Lorem Ipsum is</text>
      <text x="58" y="195" class="on-color">Lorem Ipsum is</text>
      <text x="58" y="261" class="on-color">Lorem Ipsum is</text>
      <g class="body">
        <text x="148" y="108">Short note on the topic with the key points in a simple layout for the team.</text>
        <text x="148" y="116">Each item is kept brief and to the point.</text>
        <text x="148" y="174">Short note on the topic with the key points in a simple layout for the team.</text>
        <text x="148" y="182">Each item is kept brief and to the point.</text>
        <text x="148" y="238">Short note on the topic with the key points in a simple layout for the team.</text>
        <text x="148" y="246">Each item is kept brief and to the point.</text>
      </g>
    </svg>
  </div>

  <!-- Timeline -->
  <div class="slide c3 r3">
    <svg viewBox="0 0 462 348">
      <text x="168" y="50" class="title">Lorem Ipsum is simply</text>
      <polygon points="63,174 172,174 185,194 48,194" fill="var(--blue)"/>
      <polygon points="167,174 296,174 283,194 185,194" fill="var(--lime)"/>
      <polygon points="298,174 402,174 414,194 285,194" fill="var(--cyan)"/>
      <text x="102" y="188" class="on-color">2016</text>
      <text x="223" y="187" class="on-color">2017</text>
      <text x="339" y="188" class="on-color">2018</text>
      <g class="line" stroke-width=".8">
        <line x1="112" y1="164" x2="112" y2="132"/><line x1="350" y1="164" x2="350" y2="132"/><line x1="233" y1="200" x2="233" y2="232"/>
      </g>
      <g class="body" text-anchor="middle">
        <text x="112" y="78" class="label">Lorem Ipsum</text><text x="112" y="89">is a short note on</text><text x="112" y="97">the key point and</text><text x="112" y="105">the team goal.</text><text x="112" y="113">Kept brief and</text><text x="112" y="121">clear for all.</text>
        <text x="350" y="78" class="label">Lorem Ipsum</text><text x="350" y="89">is a short note on</text><text x="350" y="97">the key point and</text><text x="350" y="105">the team goal.</text><text x="350" y="113">Kept brief and</text><text x="350" y="121">clear for all.</text>
        <text x="233" y="240" class="label">Lorem Ipsum</text><text x="233" y="251">is a short note on</text><text x="233" y="259">the key point and</text><text x="233" y="267">the team goal.</text><text x="233" y="275">Kept brief and</text><text x="233" y="283">clear for all.</text>
      </g>
    </svg>
  </div>

  <!-- Venn -->
  <div class="slide c1 r4">
    <svg viewBox="0 0 462 348">
      <text x="38" y="51" class="title">Lorem Ipsum is simply</text>
      <rect x="352" y="37" width="5" height="5" class="logo-mark"/>
      <text x="357" y="47" class="logo">Alpenrand</text>
      <circle cx="183" cy="146" r="62" fill="var(--amber)"/>
      <circle cx="280" cy="146" r="62" fill="var(--blue-mid)"/>
      <path d="M231.5,107.6 a62,62 0 0 1 0,76.8 a62,62 0 0 1 0,-76.8z" fill="#3e7f9a"/>
      <g class="icon-w">
        <circle cx="181" cy="146" r="8"/>
        <circle cx="181" cy="146" r="20"/>
        <path d="M181,122 v6 M181,164 v6 M157,146 h6 M199,146 h6 M164,129 l4,4 M194,159 l4,4 M198,129 l-4,4 M168,159 l-4,4"/>
        <path d="M272,146 a13,13 0 1 1 18,0 c-3,3 -3,6 -3,9 h-12 c0,-3 0,-6 -3,-9z"/>
        <path d="M276,160 h10 M277,165 h8"/>
        <path d="M281,117 v-5 M263,126 l-4,-3 M299,126 l4,-3"/>
      </g>
      <g class="body" text-anchor="middle">
        <text x="91" y="121" class="label">Lorem Ipsum</text><text x="91" y="131">is a short note on</text><text x="91" y="139">the key point and</text><text x="91" y="147">the team goal.</text><text x="91" y="155">Kept brief and</text><text x="91" y="163">clear for all of</text><text x="91" y="171">the staff here.</text><text x="91" y="179">Since 2016.</text>
        <text x="371" y="121" class="label">Lorem Ipsum</text><text x="371" y="131">is a short note on</text><text x="371" y="139">the key point and</text><text x="371" y="147">the team goal.</text><text x="371" y="155">Kept brief and</text><text x="371" y="163">clear for all of</text><text x="371" y="171">the staff here.</text><text x="371" y="179">Since 2016.</text>
      </g>
      <g class="body">
        <text x="27" y="225">Short note on the topic with the key points in a simple layout for the team. Each item is kept brief and to the point for all readers.</text>
        <text x="27" y="233">Content is taken from the firm website and used for finance and system topics, and also used when teaching in the class.</text>
        <text x="27" y="241">Short note on the topic with the key points in a simple layout for the team. Each item is kept brief and to the point for all readers.</text>
        <text x="27" y="249">Content is taken from the firm website and used for finance and system topics, and also used when teaching in the class.</text>
        <text x="27" y="257">Short note on the topic with the key points in a simple layout.</text>
      </g>
    </svg>
  </div>

  <!-- Pyramid -->
  <div class="slide c2 r4">
    <svg viewBox="0 0 462 348">
      <text x="166" y="51" class="title">Lorem Ipsum is simply</text>
      <polygon points="120,118 140,80 400,80 422,100 400,118" fill="var(--cyan)"/>
      <polygon points="97,162 118,122 400,122 422,143 400,162" fill="#2ec9d8"/>
      <polygon points="72,208 94,166 400,166 422,188 400,208" fill="#28a8d6"/>
      <polygon points="46,256 70,212 400,212 422,236 400,256" fill="var(--blue)"/>
      <g stroke="#fff" stroke-width="1">
        <line x1="140" y1="80" x2="156" y2="118"/><line x1="170" y1="122" x2="180" y2="162"/><line x1="190" y1="166" x2="205" y2="208"/><line x1="212" y1="212" x2="238" y2="256"/>
      </g>
      <text x="132" y="104" class="num">01</text>
      <text x="132" y="147" class="num">02</text>
      <text x="132" y="192" class="num">03</text>
      <text x="132" y="239" class="num">04</text>
      <g fill="#fff" style="font-size:4.8px">
        <text x="176" y="95" font-weight="700">Lorem Ipsum</text><text x="176" y="104">is a short note on the key points for the team.</text>
        <text x="192" y="140" font-weight="700">Lorem Ipsum</text><text x="192" y="149">is a short note on the key points for the team.</text>
        <text x="216" y="183" font-weight="700">Lorem Ipsum</text><text x="216" y="192">is a short note on the key points for the</text><text x="216" y="200">whole team.</text>
        <text x="240" y="230" font-weight="700">Lorem Ipsum</text><text x="240" y="239">is a short note on the key points</text><text x="240" y="247">for the whole team.</text>
      </g>
    </svg>
  </div>

  <!-- Wave steps -->
  <div class="slide c3 r4">
    <svg viewBox="0 0 462 348">
      <text x="166" y="51" class="title">Lorem Ipsum is simply</text>
      <rect x="352" y="37" width="5" height="5" class="logo-mark"/>
      <text x="357" y="47" class="logo">Alpenrand</text>
      <g fill="none" stroke-width="6">
        <path d="M39,146 a40,40 0 0 1 80,0" stroke="var(--lime)"/>
        <path d="M119,146 a40,40 0 0 0 80,0" stroke="var(--blue)"/>
        <path d="M199,146 a40,40 0 0 1 80,0" stroke="var(--cyan)"/>
        <path d="M279,146 a40,40 0 0 0 80,0" stroke="var(--amber)"/>
        <path d="M359,146 a40,40 0 0 1 80,0" stroke="#3a3a3a"/>
      </g>
      <circle cx="79" cy="146" r="24" fill="var(--green)"/>
      <circle cx="159" cy="146" r="24" fill="var(--blue-mid)"/>
      <circle cx="239" cy="146" r="24" fill="var(--cyan)"/>
      <circle cx="319" cy="146" r="24" fill="var(--amber)"/>
      <circle cx="399" cy="146" r="24" fill="#3a3a3a"/>
      <g class="icon-w" stroke-width="1.6">
        <circle cx="79" cy="146" r="5"/><circle cx="79" cy="146" r="11"/>
        <path d="M79,133 v3 M79,156 v3 M66,146 h3 M89,146 h3"/>
        <path d="M154,146 a8,8 0 1 1 10,0 c-2,2 -2,3 -2,5 h-6 c0,-2 0,-3 -2,-5z M156,155 h6"/>
        <circle cx="239" cy="148" r="10"/><path d="M239,148 l4,-4 M236,135 h6"/>
        <path d="M309,156 h20 M311,156 v-5 M317,156 v-9 M323,156 v-13 M310,148 l8,-7 4,3 7,-7"/>
        <rect x="389" y="138" width="16" height="16" rx="2"/><path d="M395,151 l1,-4 9,-9 3,3 -9,9z"/>
      </g>
      <g class="body" text-anchor="middle">
        <text x="159" y="72" class="label">Lorem Ipsum</text><text x="159" y="82">is a short note</text><text x="159" y="90">on the key point</text><text x="159" y="98">for the team.</text>
        <text x="319" y="72" class="label">Lorem Ipsum</text><text x="319" y="82">is a short note</text><text x="319" y="90">on the key point</text><text x="319" y="98">for the team.</text>
        <text x="79" y="186" class="label">Lorem Ipsum</text><text x="79" y="196">is a short note</text><text x="79" y="204">on the key point</text><text x="79" y="212">for the team.</text><text x="79" y="220">Kept brief.</text>
        <text x="239" y="186" class="label">Lorem Ipsum</text><text x="239" y="196">is a short note</text><text x="239" y="204">on the key point</text><text x="239" y="212">for the team.</text><text x="239" y="220">Kept brief</text><text x="239" y="228">and clear.</text>
        <text x="399" y="186" class="label">Lorem Ipsum</text><text x="399" y="196">is a short note</text><text x="399" y="204">on the key point</text><text x="399" y="212">for the team.</text><text x="399" y="220">Kept brief.</text>
      </g>
    </svg>
  </div>

</div>
</body>
</html>
```